Nodevarsity corporate powerpoint

Hi,
I am creating my own web3 and blockchain academy.

I would like to obtain pricing for a complete corporate powerpoint template for my training sessions in companies and bussiness schools

. I am sharing with you my logo in order to show you my colours.
If you can improve my logo, it will be perfect too. (full pack to launch it)

Thanks
Updates

designers are asiking for an extension

Target Market(s)

Companies and Business Schools

Industry/Entity Type

academy

Font styles to use
Sans Serif
Other font styles liked:
• Arial, Calibri

Colors
0054AA
0677BA
7BADD7
CADEEF
E8F1F8
0094D4
00A9DD
6FCCEA
C7EBF8
E9F6FB
00AB8E
00BBA5
67D7C9
C6EFE9
E9F9F6
F0912C
F2A743
F7CA91
FBE8D2
FDF5EE
EE7325
F08F49
F5BC92
FAE3D3
FDF4ED
6B429C
8869AF
B7A5CE
E3DAEB
F3F0F8

Requirements
Must have
• Blockchain thematic, withe and dark (not black) slides

```html
<!DOCTYPE html>
<html lang="en">
<head>
<meta charset="utf-8">
<title>Nodevarsity – Corporate Presentation</title>
<link rel="stylesheet" href="https://fonts.googleapis.com/css2?family=Teko:wght@500;600&family=Lato:wght@400;700&display=swap">
<style>
:root{
  --page:#ffffff;
  --deep:#1c1450;
  --violet:#2b1d78;
  --violet-2:#34248a;
  --card:#3a2a92;
  --teal:#2fe3b6;
  --teal-dark:#00ab8e;
  --purple:#6b429c;
  --text:#ffffff;
  --muted:#e6e2f5;
  --light:#f7f5fc;
  --light-card:#ebe5f4;
  --ink:#1c1450;
  --ink-soft:#453d72;
}
*{box-sizing:border-box;margin:0;padding:0}
html,body{width:1200px;height:4043px;overflow:hidden;background:var(--page)}
body{position:relative;font-family:"Lato",sans-serif;color:var(--text)}
.slide{position:absolute;left:28px;width:1139px;height:641px;overflow:hidden;
  background:linear-gradient(135deg,var(--violet) 0%,var(--violet-2) 100%);
  box-shadow:0 2px 6px rgba(0,0,0,.25)}
.slide--cover{background:radial-gradient(ellipse at 80% 20%,#3b2590 0%,transparent 55%),
  radial-gradient(ellipse at 30% 90%,#2c1f6a 0%,transparent 50%),var(--deep)}
.slide--about{background:radial-gradient(ellipse at 90% 90%,#7a67d8 0%,transparent 45%),linear-gradient(135deg,#2b1d78,#3a2a96)}
.slide--light{background:var(--light);color:var(--ink)}
.slide--light .lead{color:var(--ink-soft)}
.slide--light .accent{color:var(--teal-dark)}
.slide--light .page-no{color:var(--teal-dark)}
.frame{position:absolute;left:34px;top:19px;width:1071px;height:600px;border:3px solid var(--teal);
  border-right-color:#5a4ad6}
.slide--cover .frame{top:22px;height:597px;border-right-color:var(--teal)}
.slide--light .frame{border-color:var(--teal-dark);border-right-color:var(--purple)}
.brand{position:absolute;display:flex;align-items:center;gap:6px;background:var(--deep);
  padding:8px 10px;font-family:"Teko",sans-serif;font-weight:500;font-size:22px;line-height:1;color:var(--text)}
.brand__mark{width:10px;height:10px;background:var(--teal)}
.brand--corner{left:22px;top:19px}
.brand--center{left:50%;transform:translateX(-50%);font-size:30px;padding:14px 16px}
.h-display{position:absolute;left:0;right:0;text-align:center;font-family:"Teko",sans-serif;font-weight:600;
  font-size:84px;line-height:1;letter-spacing:1px}
.accent{color:var(--teal)}
.h-section{position:absolute;font-family:"Teko",sans-serif;font-weight:500;font-size:36px;line-height:1;letter-spacing:.5px}
.lead{position:absolute;font-size:15px;line-height:36px;color:var(--muted)}
.lead--center{text-align:center}
.lead--justify{text-align:justify}
.page-no{position:absolute;right:52px;top:592px;font-size:10px;line-height:1;color:var(--teal);letter-spacing:.5px}
.visual{position:absolute}
.visual--cube{left:589px;top:91px;width:490px;height:461px;border-radius:12px;
  background:radial-gradient(circle at 55% 50%,#8c7cf0 0%,#4b3bb0 45%,transparent 75%)}
.visual--servers{left:80px;top:70px;width:480px;height:480px;border-radius:50%;
  background:radial-gradient(circle at 50% 55%,#38b8ff 0%,#1259b8 45%,#0b2a6a 80%)}
.services{position:absolute;left:111px;top:211px;display:flex;gap:36px}
.service{width:282px;height:359px;border:3px solid var(--teal-dark);background:#ffffff;text-align:center;padding-top:22px}
.service__icon{width:100px;height:100px;border-radius:50%;margin:0 auto;
  background:linear-gradient(135deg,var(--teal) 0%,#4a6ae0 60%,var(--purple) 100%)}
.service__title{font-family:"Teko",sans-serif;font-weight:500;font-size:20px;margin-top:24px}
.service__text{font-size:12px;line-height:25.5px;margin-top:6px;padding:0 14px;color:var(--ink-soft)}
.team{position:absolute;left:69px;top:201px;display:flex;gap:28px}
.member{position:relative;width:232px;height:357px;padding-top:65px;text-align:center}
.member::before{content:"";position:absolute;left:0;right:0;top:65px;bottom:0;background:var(--light-card);border-radius:8px}
.member__photo{position:absolute;left:50%;top:0;transform:translateX(-50%);width:131px;height:131px;border-radius:50%;
  border:4px solid var(--light);background:linear-gradient(160deg,#d9d4dc,#8d8791)}
.member__body{position:relative;padding-top:82px}
.member__name{font-family:"Teko",sans-serif;font-weight:500;font-size:20px;line-height:1}
.member__role{font-size:11px;color:var(--teal-dark);margin-top:6px}
.member__text{font-size:10.5px;line-height:20px;color:var(--ink-soft);margin-top:6px;padding:0 8px}
</style>
</head>
<body>

<section class="slide slide--cover" style="top:34px">
  <div class="frame"></div>
  <div class="brand brand--center" style="top:138px"><span class="brand__mark"></span>Nodevarsity</div>
  <h1 class="h-display" style="top:258px">WELCOME TO <span class="accent">NODEVARSITY</span></h1>
  <p class="lead lead--center" style="left:118px;width:903px;top:362px">Lorem ipsum dolor sit amet, consectetur adipiscing elit, sed do eiusmod tempor incididunt ut labore et dolore magna aliqua. Quis ipsum suspendisse ultrices gravida. Risus commodo viverra maecenas accumsan lacus vel facilisis. Lorem ipsum dolor sit amet, consectetur adipiscing elit, sed do eiusmod tempor incididunt ut labore et dolore magna aliqua. Quis ipsum suspendisse ultrices gravida. Risus commodo viverra maecenas accumsan lacus vel facilisis.</p>
</section>

<section class="slide slide--about" style="top:698px">
  <div class="frame"></div>
  <div class="brand brand--corner"><span class="brand__mark"></span>Nodevarsity</div>
  <h2 class="h-section" style="left:78px;top:110px">ABOUT <span class="accent">NODEVARSITY</span></h2>
  <p class="lead lead--justify" style="left:78px;width:453px;top:155px">Lorem ipsum dolor sit amet, consectetur adipiscing elit, sed do eiusmod tempor incididunt ut labore et dolore magna aliqua. Quis ipsum suspendisse ultrices gravida. Risus commodo viverra maecenas accumsan lacus vel facilisis. Lorem ipsum dolor sit amet, consectetur adipiscing elit, sed do eiusmod tempor incididunt ut labore et dolore magna aliqua. Quis ipsum suspendisse ultrices gravida. Risus commodo viverra maecenas accumsan lacus vel facilisis. error sit voluptatem accusantium doloremque laudantium, totam rem aperiam, eaque ipsa quae ab illo inventore veritatis et quasi architecto beatae vitae dicta sunt explicabo. Nemo enim ipsam voluptatem quia voluptas sit aspernatur aut odit aut fugit, sed quia consequuntur magni dolores eos qui.</p>
  <div class="visual visual--cube" role="img" aria-label="Glowing violet 3D block cube illustration"></div>
  <span class="page-no">PAGE NO : 02</span>
</section>

<section class="slide slide--light" style="top:1361px">
  <div class="frame"></div>
  <div class="brand brand--corner"><span class="brand__mark"></span>Nodevarsity</div>
  <h2 class="h-section" style="left:0;right:0;text-align:center;top:62px">OUR <span class="accent">SERVICES</span></h2>
  <p class="lead lead--center" style="left:110px;width:920px;top:108px">Lorem ipsum dolor sit amet, consectetur adipiscing elit, sed do eiusmod tempor incididunt ut labore et dolore magna aliqua. Quis ipsum suspendisse ultrices gravida Risus commodo viverra maecenas accumsan lacus vel facilisis.</p>
  <div class="services">
    <article class="service">
      <div class="service__icon" role="img" aria-label="Blockchain cubes icon"></div>
      <h3 class="service__title">LOREM IPSUM DOLOR</h3>
      <p class="service__text">Lorem ipsum dolor sit amet, consectetur adipiscing elit, sed do eiusmod tempor incididunt ut labore et dolore magna aliqua. Ut enim ad minim veniam, quis nostrud exercitation ullamco laboris nisi ut aliquip ex ea commodo consequat.</p>
    </article>
    <article class="service">
      <div class="service__icon" role="img" aria-label="Web 3.0 browser icon"></div>
      <h3 class="service__title">LOREM IPSUM DOLOR</h3>
      <p class="service__text">Lorem ipsum dolor sit amet, consectetur adipiscing elit, sed do eiusmod tempor incididunt ut labore et dolore magna aliqua. Ut enim ad minim veniam, quis nostrud exercitation ullamco laboris nisi ut aliquip ex ea commodo consequat.</p>
    </article>
    <article class="service">
      <div class="service__icon" role="img" aria-label="Connected nodes network icon"></div>
      <h3 class="service__title">LOREM IPSUM DOLOR</h3>
      <p class="service__text">Lorem ipsum dolor sit amet, consectetur adipiscing elit, sed do eiusmod tempor incididunt ut labore et dolore magna aliqua. Ut enim ad minim veniam, quis nostrud exercitation ullamco laboris nisi ut aliquip ex ea commodo consequat.</p>
    </article>
  </div>
  <span class="page-no">PAGE NO : 03</span>
</section>

<section class="slide" style="top:2025px">
  <div class="frame"></div>
  <div class="brand brand--corner"><span class="brand__mark"></span>Nodevarsity</div>
  <div class="visual visual--servers" role="img" aria-label="Glowing blue server blocks on a circuit floor"></div>
  <h2 class="h-section" style="left:602px;top:110px">HOW <span class="accent">IT WORKS</span></h2>
  <p class="lead lead--justify" style="left:602px;width:453px;top:155px">Lorem ipsum dolor sit amet, consectetur adipiscing elit, sed do eiusmod tempor incididunt ut labore et dolore magna aliqua. Quis ipsum suspendisse ultrices gravida. Risus commodo viverra maecenas accumsan lacus vel facilisis. Lorem ipsum dolor sit amet, consectetur adipiscing elit, sed do eiusmod tempor incididunt ut labore et dolore magna aliqua. Quis ipsum suspendisse ultrices gravida. Risus commodo viverra maecenas accumsan lacus vel facilisis. error sit voluptatem accusantium doloremque laudantium, totam rem aperiam, eaque ipsa quae ab illo inventore veritatis et quasi architecto beatae vitae dicta sunt explicabo. Nemo enim ipsam voluptatem quia voluptas sit aspernatur aut odit aut fugit, sed quia consequuntur magni dolores eos qui.</p>
  <span class="page-no">PAGE NO : 04</span>
</section>

<section class="slide slide--light" style="top:2688px">
  <div class="frame"></div>
  <div class="brand brand--corner"><span class="brand__mark"></span>Nodevarsity</div>
  <h2 class="h-section" style="left:0;right:0;text-align:center;top:44px">MEET <span class="accent">OUR TEAM</span></h2>
  <p class="lead lead--center" style="left:150px;width:840px;top:90px">Lorem ipsum dolor sit amet, consectetur adipiscing elit, sed do eiusmod tempor incididunt ut labore et dolore magna aliqua. Quis ipsum suspendisse ultrices gravida Risus commodo viverra maecenas accumsan lacus .</p>
  <div class="team">
    <article class="member">
      <div class="member__photo" role="img" aria-label="Portrait photo of team member"></div>
      <div class="member__body">
        <h3 class="member__name">JOHN DEO</h3>
        <p class="member__role">Lorem ipsum dolor</p>
        <p class="member__text">Lorem ipsum dolor sit amet, consectetur adipiscing elit, sed do eiusmod tempor incididunt ut labore et dolore magna aliqua. Ut enim ad minim veniam, quis nostrud exercitation ullamco laboris nisi ut aliquip ex ea commodo consequat. Duis aute irure dolor in reprehenderit in voluptate velit .</p>
      </div>
    </article>
    <article class="member">
      <div class="member__photo" role="img" aria-label="Portrait photo of team member"></div>
      <div class="member__body">
        <h3 class="member__name">JENIFER</h3>
        <p class="member__role">Lorem ipsum dolor</p>
        <p class="member__text">Lorem ipsum dolor sit amet, consectetur adipiscing elit, sed do eiusmod tempor incididunt ut labore et dolore magna aliqua. Ut enim ad minim veniam, quis nostrud exercitation ullamco laboris nisi ut aliquip ex ea commodo consequat. Duis aute irure dolor in reprehenderit in voluptate velit .</p>
      </div>
    </article>
    <article class="member">
      <div class="member__photo" role="img" aria-label="Portrait photo of team member"></div>
      <div class="member__body">
        <h3 class="member__name">JOHN DEO</h3>
        <p class="member__role">Lorem ipsum dolor</p>
        <p class="member__text">Lorem ipsum dolor sit amet, consectetur adipiscing elit, sed do eiusmod tempor incididunt ut labore et dolore magna aliqua. Ut enim ad minim veniam, quis nostrud exercitation ullamco laboris nisi ut aliquip ex ea commodo consequat. Duis aute irure dolor in reprehenderit in voluptate velit .</p>
      </div>
    </article>
    <article class="member">
      <div class="member__photo" role="img" aria-label="Portrait photo of team member"></div>
      <div class="member__body">
        <h3 class="member__name">JENIFER</h3>
        <p class="member__role">Lorem ipsum dolor</p>
        <p class="member__text">Lorem ipsum dolor sit amet, consectetur adipiscing elit, sed do eiusmod tempor incididunt ut labore et dolore magna aliqua. Ut enim ad minim veniam, quis nostrud exercitation ullamco laboris nisi ut aliquip ex ea commodo consequat. Duis aute irure dolor in reprehenderit in voluptate velit .</p>
      </div>
    </article>
  </div>
  <span class="page-no">PAGE NO : 05</span>
</section>

<section class="slide slide--cover" style="top:3352px">
  <div class="frame"></div>
  <div class="brand brand--center" style="top:138px"><span class="brand__mark"></span>Nodevarsity</div>
  <h2 class="h-display" style="top:255px">THANK <span class="accent">YOU</span></h2>
  <p class="lead lead--center" style="left:118px;width:903px;top:358px">Lorem ipsum dolor sit amet, consectetur adipiscing elit, sed do eiusmod tempor incididunt ut labore et dolore magna aliqua. Quis ipsum suspendisse ultrices gravida. Risus commodo viverra maecenas accumsan lacus vel facilisis. Lorem ipsum dolor sit amet, consectetur adipiscing elit, sed do eiusmod tempor incididunt ut labore et dolore magna aliqua. Quis ipsum suspendisse ultrices gravida. Risus commodo viverra maecenas accumsan lacus vel facilisis.</p>
</section>

</body>
</html>
```